CD Cover Design

Listing down some requirements:

1.Pastel color scheme (ie: baby pink, light blue, light green, pale yellow, white, silver, baby pastel purple etc.) i.e: a very sweet, dreamy and girly feel

2. Name of artist: Clara Vendt
Name of Album: Lanterns: The 1st Full Length Album
(To be added into the design of the album cover, preferably name of artist in the centre middle and name of album to be below)

Note: I wish for a feminine and classy cd cover instead of a cartoony and children-like design thankyou! Hope to not have misunderstandings because I uploaded cute graphic pictures as references! Indeed I would like the cd cover to be designed by those graphic cartoons but with a feminine and classy elegant touch instead of that like a children's album. Thank you!

3. Usage of pastel cartoon designs (like the uploaded references)

Industry/Entity Type

Baby

Font styles to use
Script

Colors
d3a5cc
b768aa
eda3c7
ecdaeb
f6f0f7
cde9f5
e9f1ce
fdf9ce

Requirements
Should not have
• Over crowding of cartoons
Ie: Don't fill the whole design with the cartoons, space them out so that it don't look so messy

```html
<!DOCTYPE html>
<html lang="en">
<head>
<meta charset="utf-8">
<title>Clara Vendt — Lanterns</title>
<link rel="stylesheet" href="https://fonts.googleapis.com/css2?family=Arvo:wght@400;700&family=Sacramento&display=swap">
<style>
  :root {
    --cream: #fbfbea;
    --ink: #857d71;
    --ink-dark: #6f675d;
    --pink: #eda3c7;
    --blush: #f3c9c2;
    --sky: #cde9f5;
    --sage: #dfe9c4;
    --taupe: #c9bca8;
  }
  html, body {
    margin: 0;
    padding: 0;
    width: 1200px;
    height: 1200px;
    overflow: hidden;
    background: var(--cream);
  }
  .cover {
    position: relative;
    width: 1200px;
    height: 1200px;
    background: var(--cream);
  }
  .floral-wreath {
    position: absolute;
    left: 0;
    top: 0;
    width: 1200px;
    height: 1200px;
  }
  .artist-name {
    position: absolute;
    left: 0;
    top: 300px;
    width: 1200px;
    margin: 0;
    font-family: "Sacramento", cursive;
    font-weight: 400;
    color: var(--ink);
    -webkit-text-stroke: 3px var(--ink);
    line-height: 0.72;
    font-size: 270px;
  }
  .artist-name .first {
    display: block;
    padding-left: 330px;
  }
  .artist-name .last {
    display: block;
    padding-left: 420px;
  }
  .album {
    position: absolute;
    left: 0;
    top: 1090px;
    width: 1200px;
    text-align: center;
    font-family: "Arvo", serif;
  }
  .album-title {
    margin: 0;
    font-size: 29px;
    font-weight: 700;
    letter-spacing: 1px;
    color: var(--ink-dark);
    text-transform: uppercase;
  }
  .album-subtitle {
    margin: 6px 0 0;
    font-size: 25px;
    font-weight: 400;
    color: var(--ink);
  }
</style>
</head>
<body>
<main class="cover">
  <svg class="floral-wreath" viewBox="0 0 1200 1200" role="img" aria-label="Circular wreath of pastel flowers, leaves, hearts, butterflies and a small bird surrounding the artist name">
    <defs>
      <linearGradient id="wreathTones" x1="0" y1="0" x2="1" y2="1">
        <stop offset="0%" stop-color="#e7d9c4"/>
        <stop offset="25%" stop-color="#f3c9d6"/>
        <stop offset="45%" stop-color="#dfe9c4"/>
        <stop offset="65%" stop-color="#f5cfc6"/>
        <stop offset="82%" stop-color="#cde9f5"/>
        <stop offset="100%" stop-color="#f1c6dc"/>
      </linearGradient>
      <filter id="softEdge" x="-10%" y="-10%" width="120%" height="120%">
        <feGaussianBlur stdDeviation="28"/>
      </filter>
    </defs>
    <path class="wreath-ring"
          d="M600 20 A545 545 0 1 1 599.9 20 Z M600 230 A335 335 0 1 0 600.1 230 Z"
          fill="url(#wreathTones)" fill-rule="evenodd" opacity="0.85" filter="url(#softEdge)"/>
  </svg>

  <h1 class="artist-name">
    <span class="first">Clara</span>
    <span class="last">Vendt</span>
  </h1>

  <section class="album">
    <p class="album-title">Lanterns</p>
    <p class="album-subtitle">the 1st full length album</p>
  </section>
</main>
</body>
</html>
```